Luxury Brand Real Estate For Sale sign

**Update** I've added some examples from the internet of other signs that have a look similar to what I would like to see. I do not want my personal name in the sign. And the word FOR SALE Does not need to be so large - it can be more subtle.
I want to create a Real Estate for sale sign for my company that will be used for luxury/higher end real estate listings. I’m sharing my business card as well as a logo with new teal color to show what we're moving towards: we’re using Teal, white, black and gold.
Hoping the sign is simple, sophisticated and eye catching.
The sign should be 24" wide by 30" tall including the company name: Harbor Crest Realty Group and our logo, office phone number 727-555-0148 and website www.hcrgexample.com the words "For Sale"
Optional to add this e-mail address info@hcrgexample.com to the sign
Target Market(s)
Luxury home buyers
Industry/Entity Type
Real Estate
Look and feel

```html
<!DOCTYPE html>
<html lang="en">
<head>
<meta charset="utf-8">
<title>Harbor Crest Realty Group — For Sale Sign</title>
<link rel="stylesheet" href="https://fonts.googleapis.com/css2?family=Montserrat:wght@200;300;400;500;700&display=swap">
<style>
  :root {
    --gold: #a08400;
    --black: #000000;
    --white: #ffffff;
    --texture-light: #100e05;
  }
  html, body {
    margin: 0;
    padding: 0;
    width: 1200px;
    height: 1200px;
    overflow: hidden;
    background: var(--gold);
  }
  .sign-canvas {
    display: block;
    width: 1200px;
    height: 1200px;
    font-family: "Montserrat", sans-serif;
  }
  .backdrop { fill: var(--gold); }
  .sign-board { fill: var(--black); }
  .texture-stop-light { stop-color: var(--texture-light); }
  .texture-stop-dark { stop-color: var(--black); }
  .frame-line { stroke: var(--gold); stroke-width: 9; fill: none; stroke-linecap: butt; }
  .brand-square { fill: none; stroke: var(--white); stroke-width: 2.5; }
  .brand-name { fill: var(--white); font-weight: 300; font-size: 19px; letter-spacing: 2px; }
  .headline { fill: var(--white); font-weight: 300; font-size: 122px; }
  .phone { fill: var(--white); font-weight: 700; font-size: 52px; }
  .email { fill: var(--white); font-weight: 400; font-size: 30px; }
  .rule { stroke: var(--white); stroke-width: 5; }
  .website { fill: var(--white); font-weight: 500; font-size: 28px; }
</style>
</head>
<body>
<svg class="sign-canvas" viewBox="0 0 1200 1200" xmlns="http://www.w3.org/2000/svg" aria-label="Harbor Crest Realty Group for sale sign">
  <defs>
    <linearGradient id="board-texture" x1="0" y1="0" x2="0" y2="1">
      <stop class="texture-stop-dark" offset="0"/>
      <stop class="texture-stop-light" offset="0.5"/>
      <stop class="texture-stop-dark" offset="1"/>
    </linearGradient>
  </defs>

  <rect class="backdrop" x="0" y="0" width="1200" height="1200"/>

  <g class="sign">
    <rect class="sign-board" x="260" y="175" width="680" height="850"/>

    <rect class="board-texture" x="278" y="365" width="644" height="595" fill="url(#board-texture)"
          role="img" aria-label="Faint repeated real estate lettering as a background texture"/>

    <g class="frame">
      <path class="frame-line" d="M411 246 H331 V649"/>
      <path class="frame-line" d="M331 764 V953 H425"/>
      <path class="frame-line" d="M789 246 H869 V433"/>
      <path class="frame-line" d="M869 540 V953 H775"/>
    </g>

    <g class="brand brand-top">
      <rect class="brand-square" x="430" y="222" width="46" height="46"/>
      <text class="brand-name" x="494" y="241">HARBOR CREST</text>
      <text class="brand-name" x="494" y="265">REALTY GROUP</text>
    </g>

    <g class="listing" transform="translate(334 821) rotate(-25.2)">
      <text class="phone" x="330" y="-184" textLength="292" lengthAdjust="spacingAndGlyphs">727-555-0148</text>
      <text class="headline" x="33" y="-56" textLength="560" lengthAdjust="spacingAndGlyphs">FOR SALE</text>
      <line class="rule" x1="0" y1="0" x2="617" y2="0"/>
      <text class="email" x="17" y="51" textLength="300" lengthAdjust="spacingAndGlyphs">info@hcrgexample.com</text>
    </g>

    <text class="website" x="600" y="963" text-anchor="middle">www.hcrgexample.com</text>
  </g>

  <g class="brand brand-bottom">
    <rect class="brand-square" x="430" y="1075" width="46" height="46"/>
    <text class="brand-name" x="494" y="1094">HARBOR CREST</text>
    <text class="brand-name" x="494" y="1118">REALTY GROUP</text>
  </g>
</svg>
</body>
</html>
```